Lomi-Seret - Promote and Support a community

Design a website for Ethiopean Community. the design should be friendly, easy to navigate and maintain the look & feel of the Ethiopian culture. a proposed logo is attached but it can be change according to your recommendations. This is a project we are doing at a discount rate as it supports a weak community.
Please visit their current website http://www.lomi-seret.example.il/index.php?lang=en

Target Market(s)

Community members, potential doners

Industry/Entity Type

community

Number of Pages Required

1 page

Font styles to use
Sans Serif

Requirements
Must have
• easy to navigate friendly interface

```html
<!DOCTYPE html>
<html lang="en">
<head>
<meta charset="utf-8">
<title>Lomi-Seret – Community Health</title>
<link href="https://fonts.googleapis.com/css2?family=Poppins:wght@400;500;600;700&display=swap" rel="stylesheet">
<style>
:root{
  --maroon:#6d0000;
  --maroon-text:#7a0a0a;
  --green:#1f7f57;
  --gold:#c9ab2e;
  --ink:#222;
  --body:#3a3a3a;
  --mist:#eeeff1;
  --white:#fff;
}
*{margin:0;padding:0;box-sizing:border-box}
html,body{width:1200px;height:3509px;overflow:hidden}
body{font-family:"Poppins",sans-serif;color:var(--body);background:var(--white);position:relative}
.abs{position:absolute}
.btn{position:absolute;display:flex;align-items:center;justify-content:center;background:var(--gold);color:var(--white);font-weight:600;border-radius:26px;font-size:16px}

/* header */
.site-header{position:absolute;left:0;top:0;width:1200px;height:180px;background:var(--white)}
.brand{position:absolute;left:75px;top:68px;display:flex;align-items:center;gap:10px;font-weight:700;font-size:22px;color:var(--maroon)}
.brand-dot{width:30px;height:30px;border-radius:50%;background:var(--maroon)}
.lang{position:absolute;left:870px;top:56px;font-size:15px;font-weight:600;color:var(--ink);display:flex;align-items:center;gap:6px}
.contact-btn{left:974px;top:42px;width:152px;height:48px;font-size:16px}
.main-nav{position:absolute;top:127px;left:0;width:1200px;font-size:14px;font-weight:600;color:var(--ink)}
.main-nav span{position:absolute;white-space:nowrap}
.main-nav .active{color:#b3261e}

/* hero */
.hero{position:absolute;left:0;top:180px;width:1200px;height:726px;
  background:linear-gradient(135deg,#6e3a4a 0%,#9a3a55 35%,#7a4a6e 60%,#4e5a5a 100%)}
.hero h1{position:absolute;left:0;top:325px;width:1200px;text-align:center;color:var(--white);font-size:65px;font-weight:600}

/* feature cards */
.card{position:absolute;top:960px;width:328px;height:255px;color:var(--white);text-align:center}
.card::after{content:"";position:absolute;right:0;bottom:0;width:18px;height:18px;background:var(--white)}
.card .icon{height:60px;margin-top:34px;display:flex;align-items:center;justify-content:center}
.card h3{font-size:23px;font-weight:700;margin-top:8px;line-height:32px}
.card p{font-size:14.5px;line-height:26px;padding:0 28px;margin-top:2px}
.card a{display:inline-block;margin-top:8px;font-size:14.5px;font-weight:600;text-decoration:underline}
.card.community{left:75px;background:var(--maroon)}
.card.programs{left:436px;background:var(--green)}
.card.advocacy{left:798px;background:var(--gold)}

/* welcome */
.welcome{position:absolute;left:0;top:1294px;width:1200px;height:527px;background:var(--mist)}
.welcome h2{position:absolute;left:75px;top:62px;font-size:38px;font-weight:600;color:var(--ink)}
.welcome p{position:absolute;left:75px;top:128px;width:520px;font-size:15px;line-height:30.5px;color:var(--ink)}
.welcome .btn{left:75px;top:402px;width:178px;height:50px}

/* partners */
.partners{position:absolute;left:0;top:1821px;width:1200px;height:222px}
.partner{position:absolute;top:90px;transform:translateX(-50%);background:#d8dde6;border-radius:6px}

/* news */
.news{position:absolute;left:0;top:2043px;width:1200px;height:747px;background:var(--mist)}
.news h2{position:absolute;left:0;top:45px;width:1200px;text-align:center;font-size:38px;font-weight:600;color:var(--ink)}
.lead-story{position:absolute;left:75px;top:131px;width:512px;height:444px;background:var(--white)}
.lead-story .media{height:310px;background:linear-gradient(135deg,#b8406e,#c98a4a 55%,#7a6a8a)}
.lead-story h3{margin:22px 0 0 23px;font-size:21px;font-weight:600;color:var(--maroon-text)}
.lead-story p{margin:6px 23px 0;font-size:14.5px;line-height:26px}
.story{position:absolute;left:617px;width:510px}
.story .media{position:absolute;left:0;top:0;width:178px;height:133px}
.story h3{position:absolute;left:200px;top:-4px;width:280px;font-size:21px;line-height:31px;font-weight:600;color:var(--maroon-text)}
.story p{position:absolute;left:200px;top:66px;width:310px;font-size:14.5px;line-height:26px}
.news .btn{left:511px;top:629px;width:178px;height:52px}

/* donate band */
.donate{position:absolute;left:0;top:2790px;width:1200px;height:290px;background:var(--green);text-align:center;color:var(--white)}
.donate p{position:absolute;left:0;top:65px;width:1200px;font-size:26px;line-height:39px;font-weight:500}
.donate .btn{left:511px;top:163px;width:178px;height:50px}

/* footer */
.site-footer{position:absolute;left:0;top:3080px;width:1200px;height:429px;font-size:15px;color:var(--ink)}
.footer-brand{position:absolute;left:75px;top:110px;display:flex;align-items:center;gap:10px;font-weight:700;font-size:22px;color:var(--maroon)}
.copy{position:absolute;left:75px;top:222px;font-size:13.5px;line-height:22px}
.social{position:absolute;left:75px;top:283px;display:flex;gap:20px}
.social span{width:20px;height:20px;border-radius:50%;background:var(--maroon)}
.col{position:absolute;top:52px}
.col h4{font-size:21px;font-weight:600;color:var(--maroon-text);margin-bottom:8px}
.col li{list-style:none;line-height:34px}
.col p{line-height:29px}
.contact-row{display:flex;align-items:center;gap:18px;line-height:34px}
</style>
</head>
<body>

<header class="site-header">
  <div class="brand"><span class="brand-dot"></span>Lomi-Seret</div>
  <div class="lang">
    <svg width="15" height="15" viewBox="0 0 16 16"><circle cx="8" cy="8" r="7" fill="none" stroke="#222" stroke-width="1.6"/><path d="M1 8h14M8 1c3 3 3 11 0 14M8 1c-3 3-3 11 0 14" fill="none" stroke="#222" stroke-width="1.3"/></svg>
    EN
    <svg width="12" height="8" viewBox="0 0 12 8"><path d="M1 1l5 5 5-5" fill="none" stroke="#222" stroke-width="2"/></svg>
  </div>
  <div class="btn contact-btn">Contact Us</div>
  <nav class="main-nav">
    <span class="active" style="left:282px">HOME</span>
    <span style="left:358px">ABOUT</span>
    <span style="left:445px">THE COMMUNITY</span>
    <span style="left:605px">PROGRAMS</span>
    <span style="left:726px">NEWS</span>
    <span style="left:806px">ADVOCACY</span>
    <span style="left:926px">PARTNERS</span>
    <span style="left:1035px">SUPPORT US</span>
  </nav>
</header>

<section class="hero" role="img" aria-label="Colourful woven Ethiopian baskets seen from above">
  <h1>Welcome to Lomi-Seret</h1>
</section>

<div class="card community">
  <div class="icon"><svg width="66" height="40" viewBox="0 0 66 40" fill="#fff"><circle cx="33" cy="9" r="8"/><circle cx="15" cy="13" r="6"/><circle cx="51" cy="13" r="6"/><path d="M20 40c0-12 6-18 13-18s13 6 13 18z"/><path d="M2 38c0-9 5-14 11-14 3 0 5 1 7 3-3 3-4 7-4 11z"/><path d="M64 38c0-9-5-14-11-14-3 0-5 1-7 3 3 3 4 7 4 11z"/></svg></div>
  <h3>The Community</h3>
  <p>Sed ut perspiciatis unde omnis iste vitae dicta sunt explicabo dolorem ipsum quia dolor sit.</p>
  <a>Read More</a>
</div>
<div class="card programs">
  <div class="icon"><svg width="40" height="52" viewBox="0 0 40 52" fill="#fff"><path d="M0 0h27l13 13v39H0z"/><rect x="9" y="24" width="22" height="3" fill="#1f7f57"/><rect x="9" y="31" width="22" height="3" fill="#1f7f57"/><rect x="9" y="38" width="22" height="3" fill="#1f7f57"/></svg></div>
  <h3>Programs</h3>
  <p>Sed ut perspiciatis unde omnis iste vitae dicta sunt explicabo dolorem ipsum quia dolor sit.</p>
  <a>Read More</a>
</div>
<div class="card advocacy">
  <div class="icon"><svg width="54" height="52" viewBox="0 0 54 52" fill="#fff"><rect x="22" y="2" width="18" height="30" rx="2" transform="rotate(45 31 17)"/><rect x="-2" y="36" width="32" height="7" rx="3" transform="rotate(-45 14 40)"/></svg></div>
  <h3>Advocacy</h3>
  <p>Sed ut perspiciatis unde omnis iste vitae dicta sunt explicabo dolorem ipsum quia dolor sit.</p>
  <a>Read More</a>
</div>

<section class="welcome">
  <h2>Welcome to Lomi Seret</h2>
  <p>Aliyah (immigration) from Ethiopia to Israel and the transition to a sedentary lifestyle has resulted in the emergence of chronic diseases, in particular diabetes. While only 0.4% of the new immigrants were diagnosed with Type 2 diabetes upon arrival, by the time they had lived in Israel for ten years the figure had risen to 18% - three times as many as in the general population. The incidence of hypertension, obesity, asthma and Type 1 diabetes had also increased dramatically.</p>
  <div class="btn">Read More</div>
  <svg class="abs" style="left:545px;top:0" width="655" height="527" role="img" aria-label="Community members exercising with red balls in a health class">
    <defs><linearGradient id="class-photo" x1="0" y1="0" x2="1" y2="1"><stop offset="0" stop-color="#8aa6c4"/><stop offset=".5" stop-color="#b9ab92"/><stop offset="1" stop-color="#6b6356"/></linearGradient></defs>
    <polygon points="152,0 655,0 655,527 0,527" fill="url(#class-photo)"/>
  </svg>
</section>

<section class="partners" aria-label="Partners">
  <div class="partner" style="left:168px;width:140px;height:40px"></div>
  <div class="partner" style="left:354px;width:90px;height:80px;top:70px"></div>
  <div class="partner" style="left:528px;width:140px;height:40px"></div>
  <div class="partner" style="left:722px;width:130px;height:70px;top:75px"></div>
  <div class="partner" style="left:892px;width:100px;height:70px;top:75px"></div>
  <div class="partner" style="left:1056px;width:64px;height:110px;top:55px"></div>
</section>

<section class="news">
  <h2>Latest News</h2>
  <article class="lead-story">
    <div class="media" role="img" aria-label="Colourful woven baskets at a market stall"></div>
    <h3>Nemo enim ipsam voluptatem</h3>
    <p>Neque porro quisquam est, qui dolorem ipsum quia dolor sit amet aliquid ex ea commodi consequatu.</p>
  </article>
  <article class="story" style="top:131px">
    <div class="media" role="img" aria-label="Children gathered together" style="background:linear-gradient(135deg,#6a5a4c,#a68c70)"></div>
    <h3>Enim ipsam voluptatem quia voluptas</h3>
    <p>Neque porro quisquam est, qui dolorem ipsum quia dolor sit amet aliquid ex ea commodi consequatu.</p>
  </article>
  <article class="story" style="top:286px">
    <div class="media" role="img" aria-label="Elders at a community gathering" style="background:linear-gradient(135deg,#4a3a30,#9c8670)"></div>
    <h3>Enim ipsam voluptatem quia voluptas</h3>
    <p>Neque porro quisquam est, qui dolorem ipsum quia dolor sit amet aliquid ex ea commodi consequatu.</p>
  </article>
  <article class="story" style="top:441px">
    <div class="media" role="img" aria-label="Older man wearing a white cap" style="background:linear-gradient(135deg,#b8aa96,#5a4a3e)"></div>
    <h3>Enim ipsam voluptatem quia voluptas</h3>
    <p>Neque porro quisquam est, qui dolorem ipsum quia dolor sit amet aliquid ex ea commodi consequatu.</p>
  </article>
  <div class="btn">Read All News</div>
</section>

<section class="donate">
  <p>Lomi Seret non-profit organization operates to promote the ethiopian israel<br>comminuty healthcare, using donations and govermant funding.</p>
  <div class="btn">Support Now</div>
</section>

<footer class="site-footer">
  <div class="footer-brand"><span class="brand-dot"></span>Lomi-Seret</div>
  <div class="copy">Copyright © 2022, Company Name.<br>All Right reserved</div>
  <div class="social" aria-label="Social links"><span></span><span></span><span></span><span></span><span></span></div>

  <div class="col" style="left:358px">
    <h4>Site Map</h4>
    <ul><li>Home</li><li>About</li><li>The Community</li><li>Programs</li><li>News</li><li>Advocacy</li><li>Partners</li><li>Support Us</li></ul>
  </div>
  <div class="col" style="left:588px;width:240px">
    <h4>About Us</h4>
    <p>Lomi Seret (“health” in both Amharic and Hebrew) is dedicated to improving the health of the Ethiopian Israeli community.</p>
  </div>
  <div class="col" style="left:885px">
    <h4>Contact Us</h4>
    <p>Narkis 4/2 POB 1120<br>Migdal, 20410</p>
    <div class="contact-row"><svg width="14" height="14" viewBox="0 0 14 14"><path d="M3 1l2 3-1.5 1.5c1 2 3 4 5 5L10 9l3 2-1 2C6 13 1 8 1 2z" fill="#222"/></svg>04-6000417</div>
    <div class="contact-row"><svg width="15" height="11" viewBox="0 0 15 11"><rect width="15" height="11" rx="1" fill="#222"/><path d="M1 1l6.5 5L14 1" fill="none" stroke="#fff" stroke-width="1.3"/></svg>hello@lomi-seret.example.il</div>
  </div>
</footer>

</body>
</html>
```